Small beauty therapy room here in melbourne needs a simple but classy business card

I am after business cards for a small beauty therapy room operating from a hair salon in a rich area of melbourne. My main job is waxing, facials and tinting.

Target Market(s)

all ages

Industry/Entity Type

Beauty Salon

Contact Information for Business Card

The name of the business is Marisol's Beauty Room id like this on the front with a pattern of some kind but still simple.
I am after a business card that is either white and silver/icy green, or a dark charcoal grey with icy green colour and pattern, or even black and white, I'm quite flexible.

On the back id like it to have
Marisol Quenteli
Beauty Therapist

contact number: 0412 963 174
email: marisolquenteli@examplemail.net
website: www.marisolsbeautyroom.example.au

address:3/218-226 Ferrow Rd, Kelsby VIC 3187
with the Chatterbook and snapfolio logos only
I'm very flexible and open so anything creative and simple would be great :)

Font styles to use
Serif
Sans Serif
Decorative

Colors
cfeae6
ffffff
c6c6c6

Requirements
Must have
• classy, elegance, simple

```html
<!DOCTYPE html>
<html lang="en">
<head>
<meta charset="utf-8">
<title>Marisol's Beauty Room – Business Card</title>
<link href="https://fonts.googleapis.com/css2?family=Great+Vibes&family=Questrial&display=swap" rel="stylesheet">
<style>
  :root {
    --backdrop: #1b1b1b;
    --card: #3b3b3d;
    --card-light: #444446;
    --icy-green: #cfeae6;
    --silver: #c6c6c6;
    --white: #ffffff;
  }
  * { box-sizing: border-box; margin: 0; padding: 0; }
  html, body {
    width: 1200px; height: 1076px; overflow: hidden;
    background: var(--backdrop);
    font-family: "Questrial", "Century Gothic", sans-serif;
  }
  .stage {
    position: relative; width: 1200px; height: 1076px;
    display: flex; flex-direction: column; align-items: center; justify-content: center; gap: 44px;
  }
  .card {
    position: relative; width: 860px; height: 478px;
    border-radius: 4px; overflow: hidden;
    box-shadow: 0 18px 40px rgba(0,0,0,.55);
  }
  .card-texture {
    position: absolute; inset: 0;
    background: radial-gradient(ellipse at 40% 35%, var(--card-light), var(--card) 70%);
  }
  .brand {
    position: absolute; display: flex; align-items: center; gap: 18px;
    color: var(--silver); font-family: "Questrial", sans-serif;
  }
  .brand-dot {
    width: 26px; height: 26px; border-radius: 50%; background: var(--icy-green); flex: none;
  }
  .brand-name { line-height: 1; }
  .brand-name .line-main { display: block; font-size: 74px; letter-spacing: 1px; }
  .brand-name .line-sub { display: block; font-size: 32px; letter-spacing: 3px; margin-top: 6px; padding-left: 4px; }

  /* front */
  .card-front .brand { left: 50%; top: 118px; transform: translateX(-50%); }
  .card-front .web {
    position: absolute; left: 0; right: 0; top: 330px; text-align: center;
    color: var(--white); font-size: 26px; letter-spacing: 1px;
  }

  /* back */
  .card-back .brand { left: 58px; top: 52px; }
  .card-back .rule {
    position: absolute; left: 58px; top: 262px; width: 560px; height: 2px; background: var(--icy-green);
  }
  .contact-list { position: absolute; left: 50px; top: 292px; list-style: none; }
  .contact-list li {
    display: flex; align-items: center; gap: 14px;
    color: var(--white); font-size: 24px; letter-spacing: .5px; height: 38px;
  }
  .contact-icon {
    width: 30px; height: 30px; border-radius: 50%; flex: none;
    border: 2px solid var(--icy-green); display: flex; align-items: center; justify-content: center;
  }
  .contact-icon svg { width: 16px; height: 16px; }
  .person { position: absolute; right: 46px; top: 222px; text-align: right; }
  .person-name { font-family: "Great Vibes", cursive; color: var(--white); font-size: 44px; line-height: 1; }
  .person-role { color: var(--icy-green); font-size: 26px; letter-spacing: .5px; margin-top: 2px; }
  .address {
    position: absolute; right: 46px; top: 370px; text-align: right;
    color: var(--white); font-size: 25px; line-height: 1.3; letter-spacing: .5px;
  }
</style>
</head>
<body>
<main class="stage">
  <section class="card card-front">
    <div class="card-texture" role="img" aria-label="Charcoal card stock with a subtle embossed swirl pattern"></div>
    <div class="brand">
      <span class="brand-dot"></span>
      <span class="brand-name"><span class="line-main">Marisol's</span><span class="line-sub">Beauty Room</span></span>
    </div>
    <p class="web">www.marisolsbeautyroom.example.au</p>
  </section>

  <section class="card card-back">
    <div class="card-texture" role="img" aria-label="Charcoal card stock with a subtle embossed swirl pattern"></div>
    <div class="brand">
      <span class="brand-dot"></span>
      <span class="brand-name"><span class="line-main">Marisol's</span><span class="line-sub">Beauty Room</span></span>
    </div>
    <div class="rule"></div>
    <ul class="contact-list">
      <li>
        <span class="contact-icon"><svg viewBox="0 0 16 16"><path d="M3 2h3l1 3-2 1.5a8 8 0 0 0 4.5 4.5L11 9l3 1v3a1 1 0 0 1-1 1A12 12 0 0 1 2 3a1 1 0 0 1 1-1z" fill="#cfeae6"/></svg></span>
        0412 963 174
      </li>
      <li>
        <span class="contact-icon"><svg viewBox="0 0 16 16"><rect x="1.5" y="3.5" width="13" height="9" fill="none" stroke="#cfeae6" stroke-width="1.5"/><path d="M1.5 3.5 8 9l6.5-5.5" fill="none" stroke="#cfeae6" stroke-width="1.5"/></svg></span>
        marisolquenteli@examplemail.net
      </li>
      <li>
        <span class="contact-icon"><svg viewBox="0 0 16 16"><circle cx="8" cy="8" r="6.5" fill="none" stroke="#cfeae6" stroke-width="1.3"/><ellipse cx="8" cy="8" rx="2.8" ry="6.5" fill="none" stroke="#cfeae6" stroke-width="1.1"/><path d="M1.5 8h13" stroke="#cfeae6" stroke-width="1.1"/></svg></span>
        www.marisolsbeautyroom.example.au
      </li>
    </ul>
    <div class="person">
      <p class="person-name">Marisol Quenteli</p>
      <p class="person-role">Beauty Therapist</p>
    </div>
    <p class="address">3/218-226 Ferrow Rd,<br>Kelsby VIC 3187</p>
  </section>
</main>
</body>
</html>
```